Derek Holloway Plumbing and Heating

Need a card design for a plumbing and heating company that does service and repair, remodels, and plumbing in new construction. Please add following on back side of card; Boilers, Water heaters, Gas lines, Sump pumps, Toilet repairs, Faucet repairs, Pipe thawing, Radiant heating, New construction, Remodels.

Industry/Entity Type

Plumber

Contact Information for Business Card

Was thinking white gloss card with colored logo in middle or black glossy card with silver logo in middle. Just a thought but very open to other designs.

Requirements
Must have
• Need following on front of card;
• P(203) 321-8689
• C(203) 232-9069
• Derek Holloway 62 Marlow Ave North, Stamford, Ct 06455
• service@TorvenFlow.com (plumbing in blue, heating in red)
• www.TorvenFlow.com (plumbing in blue, heating in red)
• Fully Licensed and Insured
Nice to have
• Elegant design

```html
<!DOCTYPE html>
<html lang="en">
<head>
<meta charset="utf-8">
<title>Derek Holloway Plumbing and Heating – Business Card</title>
<link href="https://fonts.googleapis.com/css2?family=Open+Sans:wght@400;600;700&display=swap" rel="stylesheet">
<style>
  :root {
    --bg: #e9e7e4;
    --card-white: #ffffff;
    --card-black: #0b0b0c;
    --blue: #2f62b8;
    --red: #d62e3a;
    --ink: #1e1e1e;
    --grey: #555555;
    --silver: #c9ccd2;
  }
  * { box-sizing: border-box; margin: 0; padding: 0; }
  html, body { width: 1200px; height: 913px; overflow: hidden; }
  body {
    background: var(--bg);
    font-family: "Open Sans", Arial, sans-serif;
    position: relative;
  }
  .card {
    position: absolute;
    width: 540px;
    height: 309px;
    border-radius: 14px;
    overflow: hidden;
    box-shadow: 0 6px 18px rgba(0,0,0,.18);
  }
  .card-front { left: 40px; top: 302px; background: var(--card-white); }
  .card-back  { left: 620px; top: 302px; background: var(--card-black); }

  .edge-bands { position: absolute; left: 0; bottom: 0; width: 540px; height: 40px; }

  /* front */
  .brand-name {
    position: absolute;
    left: 34px; top: 92px;
    width: 230px;
    font-weight: 700;
    font-size: 22px;
    line-height: 1.15;
    color: var(--blue);
    text-transform: uppercase;
    display: flex; align-items: center; gap: 10px;
  }
  .brand-dot { flex: none; width: 14px; height: 14px; border-radius: 50%; background: var(--blue); }
  .holder { position: absolute; right: 34px; top: 30px; text-align: right; }
  .holder-name { font-size: 21px; font-weight: 700; color: var(--ink); letter-spacing: .5px; }
  .holder-role { font-size: 11px; color: var(--red); text-transform: uppercase; letter-spacing: 1px; }
  .address {
    position: absolute; right: 34px; top: 92px; text-align: right;
    font-size: 11.5px; line-height: 1.45; color: var(--ink);
  }
  .divider { position: absolute; height: 1px; background: var(--ink); }
  .divider-right { right: 34px; top: 134px; width: 230px; }
  .divider-left { left: 34px; top: 240px; width: 200px; }
  .contacts {
    position: absolute; right: 34px; top: 146px; text-align: right;
    font-size: 11.5px; line-height: 1.55; color: var(--ink);
  }
  .contact-row { display: flex; justify-content: flex-end; align-items: center; gap: 6px; }
  .contact-row svg { width: 11px; height: 11px; flex: none; }
  .contact-web { font-weight: 600; font-size: 12.5px; }
  .tone-blue { color: var(--blue); }
  .tone-red { color: var(--red); }
  .licensed {
    position: absolute; left: 34px; top: 248px;
    font-size: 13px; font-weight: 600; color: var(--blue);
  }

  /* back */
  .gloss {
    position: absolute; inset: 0;
    background: linear-gradient(115deg, rgba(255,255,255,0) 35%, rgba(255,255,255,.08) 48%, rgba(255,255,255,0) 60%);
  }
  .back-brand {
    position: absolute; right: 40px; top: 78px; width: 250px;
    font-weight: 700; font-size: 22px; line-height: 1.15;
    color: var(--silver); text-transform: uppercase;
    display: flex; align-items: center; gap: 10px;
  }
  .back-brand .brand-dot { background: var(--silver); }
  .services {
    position: absolute; left: 36px; top: 112px;
    list-style: none; font-size: 13px; line-height: 1.32; color: #ffffff;
  }
  .services li { display: flex; align-items: center; gap: 9px; }
  .services li::before {
    content: ""; width: 8px; height: 8px; border-radius: 50%; background: var(--blue); flex: none;
  }
</style>
</head>
<body>

<section class="card card-front" aria-label="Business card front">
  <div class="brand-name"><span class="brand-dot"></span><span>Derek Holloway Plumbing and Heating</span></div>

  <div class="holder">
    <div class="holder-name">ALAN PRYCE</div>
    <div class="holder-role">Owner</div>
  </div>

  <div class="address">Derek Holloway 62 Marlow Ave North,<br>Stamford, Ct 06455</div>
  <div class="divider divider-right"></div>

  <div class="contacts">
    <div class="contact-row">(203) 555-4172
      <svg viewBox="0 0 12 12"><path d="M3 1l2 2.5-1.2 1.2a6 6 0 0 0 3.5 3.5L8.5 7 11 9l-1.3 2C5 11 1 7 1 2.3z" fill="var(--red)"/></svg>
    </div>
    <div class="contact-row">(203) 555-7830
      <svg viewBox="0 0 12 12"><rect x="3" y="1" width="6" height="10" rx="1" fill="none" stroke="var(--red)" stroke-width="1.3"/></svg>
    </div>
    <div class="contact-row">service@<span class="tone-blue">Torven</span><span class="tone-red">Flow</span>.com
      <svg viewBox="0 0 12 12"><rect x="1" y="2.5" width="10" height="7" fill="none" stroke="var(--red)" stroke-width="1.2"/><path d="M1 2.5l5 4 5-4" fill="none" stroke="var(--red)" stroke-width="1.2"/></svg>
    </div>
    <div class="contact-row contact-web">www.<span class="tone-blue">Torven</span><span class="tone-red">Flow</span>.com
      <svg viewBox="0 0 12 12"><circle cx="6" cy="6" r="5" fill="none" stroke="var(--red)" stroke-width="1.2"/><path d="M1 6h10M6 1c-3 3-3 7 0 10M6 1c3 3 3 7 0 10" fill="none" stroke="var(--red)" stroke-width=".9"/></svg>
    </div>
  </div>

  <div class="divider divider-left"></div>
  <div class="licensed">Fully Licensed and Insured</div>

  <svg class="edge-bands" viewBox="0 0 540 40" aria-hidden="true">
    <polygon points="0,26 300,26 300,40 0,40" fill="var(--blue)"/>
    <polygon points="286,12 540,12 540,40 300,40 300,26" fill="var(--red)"/>
    <polygon points="286,12 300,26 286,26" fill="var(--blue)"/>
  </svg>
</section>

<section class="card card-back" aria-label="Business card back">
  <div class="gloss"></div>
  <div class="back-brand"><span class="brand-dot"></span><span>Derek Holloway Plumbing and Heating</span></div>

  <ul class="services">
    <li>Boilers</li>
    <li>Water heaters</li>
    <li>Gas lines</li>
    <li>Sump pumps</li>
    <li>Toilet repairs</li>
    <li>Faucet repairs</li>
    <li>Pipe thawing</li>
    <li>Radiant heating</li>
    <li>New construction</li>
    <li>Remodels</li>
  </ul>

  <svg class="edge-bands" viewBox="0 0 540 40" aria-hidden="true">
    <rect x="0" y="28" width="300" height="12" fill="#ffffff"/>
    <rect x="300" y="28" width="240" height="12" fill="var(--blue)"/>
  </svg>
</section>

</body>
</html>
```